Halvercott Orthodontics business card

Using our existing logo (created with ArtFolio), please create a tasteful, contemporary business card. We are father and daughter orthodontists specializing in braces, clarafit, etc to design healthy, beautiful smiles for children, adolescents, and adults. We would like the design to be family-friendly but not childish.
The final design should include all of the information without looking cluttered (I hope! If necessary to achieve an optimal design, please consider making the card double-sided)
Purple, black, silver on a white card
Please include the following information:
Halvercott Orthodontics (logo)
Marguerite L. Halvercott, DMD
Douglas R. Halvercott, DMD

312 Bramblewood Street
Linden Falls, MA 01899
978.555.0142

847C Quarry Hollow Street
Ashgrove, MA 01898
978.555.0187

email frontdesk@halvercottortho.example
website www.halvercottortho.example

```html
<!DOCTYPE html>
<html lang="en">
<head>
<meta charset="utf-8">
<title>Halvercott Orthodontics business card</title>
<link rel="stylesheet" href="https://fonts.googleapis.com/css2?family=Montserrat:wght@400;500&display=swap">
<style>
  :root {
    --stage: #ebebeb;
    --purple: #672d8e;
    --white: #ffffff;
    --ink: #2b2b2b;
    --divider: rgba(255,255,255,0.35);
  }
  * { box-sizing: border-box; margin: 0; padding: 0; }
  html, body {
    width: 1200px; height: 1164px; overflow: hidden;
    background: var(--stage);
    font-family: "Montserrat", sans-serif;
  }
  .sheet {
    width: 1200px; height: 1164px;
    display: flex; align-items: center; justify-content: center; gap: 40px;
  }
  .card {
    position: relative;
    width: 540px; height: 324px;
    box-shadow: 0 1px 3px rgba(0,0,0,0.12);
  }
  .card--front { background: var(--purple); color: var(--white); }
  .card--back { background: var(--white); color: var(--ink); }

  .brand {
    display: flex; align-items: center; gap: 10px;
    font-weight: 500; font-size: 26px; letter-spacing: 0.5px; white-space: nowrap;
  }
  .brand__dot { width: 14px; height: 14px; border-radius: 50%; flex: none; }
  .card--front .brand {
    position: absolute; top: 112px; left: 0; right: 0; justify-content: center;
    color: var(--white);
  }
  .card--front .brand__dot { background: var(--white); }
  .card--back .brand {
    position: absolute; top: 48px; left: 60px; color: var(--purple); font-size: 23px;
  }
  .card--back .brand__dot { background: var(--purple); }

  .locations {
    position: absolute; left: 0; right: 0; bottom: 34px;
    display: flex; justify-content: center; align-items: stretch;
  }
  .location {
    width: 232px; text-align: center; font-style: normal;
    font-size: 12.5px; line-height: 18px;
  }
  .locations__divider { width: 1px; background: var(--divider); margin: 0 12px; }

  .doctors {
    position: absolute; top: 152px; left: 68px;
    font-size: 15.5px; line-height: 22px;
  }
  .contact {
    position: absolute; top: 246px; left: 68px;
    font-size: 14px; line-height: 19px;
  }
</style>
</head>
<body>
<main class="sheet">
  <section class="card card--front" aria-label="Card front">
    <div class="brand"><span class="brand__dot"></span>Halvercott Orthodontics</div>
    <div class="locations">
      <address class="location">
        847C Quarry Hollow Street<br>Ashgrove, MA 01898<br>978.555.0187
      </address>
      <span class="locations__divider"></span>
      <address class="location">
        312 Bramblewood Street<br>Linden Falls, MA 01899<br>978.555.0142
      </address>
    </div>
  </section>

  <section class="card card--back" aria-label="Card back">
    <div class="brand"><span class="brand__dot"></span>Halvercott Orthodontics</div>
    <p class="doctors">Marguerite L. Halvercott, DMD<br>Douglas R. Halvercott, DMD</p>
    <p class="contact">frontdesk@halvercottortho.example<br>www.halvercottortho.example</p>
  </section>
</main>
</body>
</html>
```